Profesional personal website needs design and business card

I need a business card with my professional name as a logo "Marlo Vitality" for my business. I am a Wellness Coach, consultant and trainer. So it should be professional, wellness oriented and modern.

Target Market(s)

Private clients, governments, corporations. Luxury and high market.

Industry/Entity Type

Health And Wellness

Contact Information for Business Card

Marlo Vitality should be the logo

Colors

Designer to choose colors to be used in the design.

Requirements
Must have
• Marlo Vitality
• Name: Tomás Arribal
• Wellness Coach, Consultant & Trainer.
• Website: www.marlovitality.example
• Phone:
• Spain (+34) 612 480 397
• (USA) +1 (555) 318 2046
Nice to have
• The most important is the design of "Marlo Vitality", as this is going to be my personal brand logo. It should be professional, wellness, high end and actual.
Should not have
• no golds, no baroque style..

```html
<!DOCTYPE html>
<html lang="en">
<head>
<meta charset="utf-8">
<title>Marlo Vitality — Business Card</title>
<link rel="stylesheet" href="https://fonts.googleapis.com/css2?family=Montserrat:ital,wght@0,400;0,500;0,700;1,400&family=Sacramento&display=swap">
<style>
  :root {
    --coral: #ea5d51;
    --navy: #333744;
    --stone: #c9c6c1;
    --ink-light: #ffffff;
    --backdrop: #e8e4de;
    --script: "Sacramento", cursive;
    --sans: "Montserrat", sans-serif;
  }
  * { margin: 0; padding: 0; box-sizing: border-box; }
  html, body {
    width: 1200px;
    height: 1200px;
    overflow: hidden;
    background: var(--backdrop);
  }
  .sheet {
    position: relative;
    width: 1200px;
    height: 1200px;
  }
  .card {
    position: absolute;
    left: 175px;
    width: 850px;
    height: 473px;
  }
  .card--front {
    top: 80px;
    background: var(--coral);
    display: flex;
    align-items: center;
    justify-content: center;
  }
  .card--back {
    top: 648px;
    background: var(--navy);
  }
  .website {
    font-family: var(--script);
    font-size: 74px;
    font-weight: 400;
    color: var(--ink-light);
    letter-spacing: 1px;
    transform: translateY(-12px);
  }
  .brand {
    position: absolute;
    left: 76px;
    top: 54px;
    font-family: var(--sans);
    font-weight: 700;
    font-size: 42px;
    color: var(--coral);
    letter-spacing: 0.5px;
    line-height: 1;
  }
  .identity {
    position: absolute;
    right: 67px;
    top: 190px;
    text-align: right;
  }
  .identity__name {
    font-family: var(--script);
    font-size: 72px;
    color: var(--ink-light);
    line-height: 1;
    margin-right: 20px;
  }
  .identity__role {
    font-family: var(--sans);
    font-size: 18px;
    font-weight: 400;
    color: var(--stone);
    letter-spacing: 2.6px;
    margin-top: -4px;
    margin-right: 19px;
  }
  .contacts {
    position: absolute;
    left: 442px;
    right: 67px;
    top: 378px;
    font-size: 20px;
    line-height: 26px;
  }
  .contacts__row {
    display: flex;
    justify-content: space-between;
  }
  .contacts__region {
    font-family: var(--sans);
    font-style: italic;
    color: var(--coral);
    letter-spacing: 1px;
  }
  .contacts__phone {
    font-family: var(--sans);
    color: var(--stone);
    letter-spacing: 2px;
  }
</style>
</head>
<body>
  <main class="sheet">
    <section class="card card--front">
      <p class="website">www.marlovitality.example</p>
    </section>

    <section class="card card--back">
      <h1 class="brand">Marlo Vitality</h1>

      <div class="identity">
        <p class="identity__name">Tomás Arribal</p>
        <p class="identity__role">Wellness Coach, Consultant &amp; Trainer</p>
      </div>

      <div class="contacts">
        <p class="contacts__row">
          <span class="contacts__region">Spain.</span>
          <span class="contacts__phone">(+34) 612 480 397</span>
        </p>
        <p class="contacts__row">
          <span class="contacts__region">USA.</span>
          <span class="contacts__phone">+1 (555) 318 2046</span>
        </p>
      </div>
    </section>
  </main>
</body>
</html>
```